Looking for a full stationery set design for our business - NO generic/stock templates please.

I am looking for a complete stationary set for my used car dealership. I am looking for something, unique, creative, classy and high-end. Generic designs or anything that looks like a 'stock' template will not be selected. Please do not use a vehicle image in the design - - that is too predictable for a car dealership.

I prefer matte designs over shiny/glossy designs but will consider both if the look is right. I have attached a few different variations of our logo you can work with, as well as a QR code to our website.

These are the items needed:
- Letterhead (with MS word file)
- Envelope #10
- Envelope 9" x 12"
- Envelope 10" x 13"
- Presentation Folder 9" x 12"
- Business Cards 2" x 3.5"
- Folded Card (5.5 x 8" folded to 4" x 5.5")
- Notepad Small (4" x 6")
- Notepad Large (5.5" x 8.5")
- Postcard (4" x 6")

Low design entries Many entries from the same designers Many repetitive designs Too many generic entries that look like stock templates

• Original, creative work, high-end/classy appeal. Must stand out as high-quality, professional image that captures your attention.
• No generic/stock templates or anything that looks like it.

```html
<!DOCTYPE html>
<html lang="en">
<head>
<meta charset="utf-8">
<title>Ridgeway Auto – Business Card</title>
<link rel="stylesheet" href="https://fonts.googleapis.com/css2?family=Open+Sans:wght@400;600;800&display=swap">
<style>
  :root {
    --backdrop-top: #4a4a4a;
    --backdrop-bottom: #1e1e1e;
    --card: #2a2a2b;
    --card-edge: #1c1c1d;
    --ink: #f2f2f2;
    --accent: #1f8ad6;
    --faint: #333334;
    --gloss: #5a5a5c;
  }
  * { box-sizing: border-box; margin: 0; padding: 0; }
  html, body { width: 1200px; height: 960px; overflow: hidden; }
  body {
    background: radial-gradient(ellipse at 50% 30%, var(--backdrop-top), var(--backdrop-bottom));
    font-family: "Open Sans", Arial, sans-serif;
    position: relative;
  }
  .card {
    position: absolute;
    left: 320px;
    width: 560px;
    height: 320px;
    background: var(--card);
    box-shadow: 0 3px 0 var(--card-edge), 0 6px 0 var(--card-edge), 0 18px 30px rgba(0,0,0,.5);
    overflow: hidden;
  }
  .card--front { top: 80px; display: flex; align-items: center; justify-content: center; }
  .card--back { top: 520px; }

  .front-name {
    font-weight: 800;
    font-size: 54px;
    color: var(--gloss);
    letter-spacing: 1px;
  }

  .watermark {
    position: absolute;
    left: 22px;
    top: 4px;
    font-weight: 800;
    font-size: 92px;
    line-height: 1.1;
    color: var(--faint);
    white-space: nowrap;
  }

  .brand {
    position: absolute;
    right: 30px;
    top: 132px;
    display: flex;
    align-items: center;
    gap: 8px;
    font-weight: 800;
    font-size: 20px;
    line-height: 26px;
    color: var(--accent);
  }
  .brand-dot { width: 11px; height: 11px; border-radius: 50%; background: var(--accent); }

  .rule {
    position: absolute;
    left: 0; right: 30px;
    top: 174px;
    height: 1.5px;
    background: var(--accent);
  }

  .person { position: absolute; left: 30px; top: 186px; }
  .person-name { color: var(--accent); font-size: 18px; line-height: 24px; font-weight: 600; }
  .person-role { color: var(--ink); font-size: 14px; line-height: 19px; margin-bottom: 6px; }
  .contact-list { list-style: none; }
  .contact-list li {
    display: flex; align-items: center; gap: 8px;
    color: var(--ink); font-size: 14px; line-height: 20px;
  }
  .contact-list svg { width: 11px; height: 11px; flex: none; }
  .icon-fill { fill: var(--accent); }
  .icon-line { fill: none; stroke: var(--accent); stroke-width: 2.5; }

  .address { position: absolute; left: 268px; top: 186px; }
  .address-label { color: var(--accent); font-size: 15px; line-height: 22px; font-weight: 600; }
  .address-line { color: var(--ink); font-size: 14px; line-height: 19px; }
</style>
</head>
<body>
  <section class="card card--front" aria-label="Business card front">
    <span class="front-name">Ridgeway Auto</span>
  </section>

  <section class="card card--back" aria-label="Business card back">
    <div class="watermark" aria-hidden="true">Ridgeway</div>

    <div class="brand"><span class="brand-dot"></span>Ridgeway Auto</div>

    <div class="rule"></div>

    <div class="person">
      <p class="person-name">Daniel R. Hale</p>
      <p class="person-role">Founder &amp; CEO</p>
      <ul class="contact-list">
        <li>
          <svg viewBox="0 0 24 24"><path class="icon-fill" d="M6.6 10.8a15.1 15.1 0 0 0 6.6 6.6l2.2-2.2c.3-.3.7-.4 1-.2 1.1.4 2.3.6 3.6.6.6 0 1 .4 1 1V20c0 .6-.4 1-1 1A17 17 0 0 1 3 4c0-.6.4-1 1-1h3.5c.6 0 1 .4 1 1 0 1.3.2 2.5.6 3.6.1.3 0 .7-.2 1z"/></svg>
          000 000 0000
        </li>
        <li>
          <svg viewBox="0 0 24 24"><path class="icon-line" d="M3 6h18v12H3z M3 6l9 7 9-7"/></svg>
          RidgewayAuto.com
        </li>
        <li>
          <svg viewBox="0 0 24 24"><circle class="icon-fill" cx="12" cy="12" r="10"/></svg>
          dan@RidgewayAuto.com
        </li>
      </ul>
    </div>

    <div class="address">
      <p class="address-label">Address:</p>
      <p class="address-line">1418 Birch Lane</p>
      <p class="address-line">Cedarport, MI 48621</p>
    </div>
  </section>
</body>
</html>
```